Orthodox Christian Youth Conference Flyer/Agenda

We are seeking a designer to help us take our award winning conference to the next level with a pamphlet that will outline the agenda of the 3 day conference but will also include pictures, illustrations, and visuals so that we build some excitement and interest. We also need to be able to make adjustments and corrections to the pamphlet's text, leading up to the conference and would like it in a file that could permit us to edit it without having to bother you!

Target Market(s)

To be used to promote conference and agenda

Industry/Entity Type

Christian

Font styles to use
Serif
Sans Serif

Requirements
Must have
• include logo, photos and visuals

```html
<!DOCTYPE html>
<html lang="en">
<head>
<meta charset="utf-8">
<title>Faith and Fellowship Family Gathering – Agenda Pamphlet</title>
<link rel="stylesheet" href="https://fonts.googleapis.com/css2?family=Open+Sans:wght@400;600;700;800&family=Merriweather:wght@400;700&display=swap">
<style>
:root{
  --backdrop:#5b4330;
  --page:#ffffff;
  --forest:#1f3a17;
  --olive:#3f5f1c;
  --lime:#8dc63f;
  --ink:#2b2b2b;
  --muted:#5a5a5a;
  --photo-warm:#b89a6a;
  --photo-cool:#6f8a5a;
}
*{margin:0;padding:0;box-sizing:border-box}
html,body{width:889px;height:1200px;overflow:hidden}
body{background:var(--backdrop);font-family:"Open Sans",Arial,sans-serif;color:var(--ink);position:relative}
.page{position:absolute;background:var(--page);overflow:hidden;box-shadow:0 3px 10px rgba(0,0,0,.35)}
.page-1{left:83px;top:30px;width:355px;height:475px}
.page-2{left:453px;top:30px;width:362px;height:475px}
.page-3{left:222px;top:578px;width:460px;height:532px}
.page-label{position:absolute;color:#fff;font-weight:800;font-size:15px;letter-spacing:.5px}
.abs{position:absolute}
.photo{position:absolute}
.header{left:0;top:0;width:175px;height:100px;background:var(--forest);padding:8px 10px;display:flex;flex-direction:column;gap:4px}
.parish-name{color:#fff;font-weight:800;font-size:9px;line-height:1.15;text-transform:uppercase}
.conf-title{color:var(--lime);font-weight:700;font-size:7px;line-height:1.25}
.conf-theme{color:#e8f2d8;font-size:5.8px}
.band{background:var(--forest);color:#fff;font-weight:800;text-transform:uppercase;line-height:1.05;display:flex;align-items:center;justify-content:center;text-align:center;border-bottom:4px solid var(--lime);border-radius:0 0 22px 0}
.agenda{font-size:5.6px;line-height:1.55;color:var(--ink)}
.agenda h4{font-size:6.4px;color:var(--olive);font-weight:800;margin-top:5px}
.agenda h4:first-child{margin-top:0}
.agenda li{list-style:none;padding-left:7px;position:relative}
.agenda li::before{content:"";position:absolute;left:1px;top:3px;width:3px;height:3px;background:var(--lime);border-radius:50%}
.donate{background:var(--forest);color:#fff;padding:8px;text-align:center}
.donate h3{font-family:"Merriweather",Georgia,serif;font-size:15px;color:var(--lime);letter-spacing:1px}
.donate p{font-size:6px;line-height:1.4;margin-top:4px}
.donate .mark{display:inline-flex;align-items:center;gap:3px;margin-top:5px;font-size:6px;font-weight:700}
.donate .mark i{width:6px;height:6px;background:var(--lime);display:inline-block}
.strip{left:0;bottom:0;width:100%;height:26px;background:var(--lime);color:var(--forest);font-size:6.5px;font-weight:700;display:flex;align-items:center;padding:0 12px}
.body-text{font-size:5.8px;line-height:1.5;color:var(--muted)}
.body-text p{margin-bottom:4px}
.body-text b{color:var(--olive)}
.faq h4{font-family:"Merriweather",Georgia,serif;font-size:11px;color:var(--forest);margin-bottom:5px}
.page-3 .body-text{font-size:6.3px;line-height:1.55}
</style>
</head>
<body>

<section class="page page-1">
  <div class="abs header">
    <div class="parish-name">The Parish of St. Andrew and Luke Orthodox Christian Church</div>
    <div class="conf-title">The Faith and Fellowship Family Gathering, Millbrook, Pennsylvania</div>
    <div class="conf-theme">Theme: Growing Together in Christ</div>
  </div>
  <div class="photo" role="img" aria-label="Photo of clergy leading an outdoor procession" style="left:175px;top:0;width:180px;height:100px;background:linear-gradient(135deg,#d8cbb0,var(--photo-warm) 60%,#6d5a3c)"></div>

  <div class="abs band" style="left:12px;top:112px;width:150px;height:44px;font-size:11px">Preliminary<br>Program Agenda</div>

  <ul class="abs agenda" style="left:14px;top:166px;width:160px">
    <h4>Thursday, October 8th</h4>
    <li>4:00 pm – Registration and Welcome Desk Opens</li>
    <li>6:00 pm – Vespers in the Parish Church</li>
    <li>7:00 pm – Opening Dinner and Greetings</li>
    <li>8:30 pm – Youth Icebreakers in Fellowship Hall</li>
    <h4>Friday, October 9th</h4>
    <li>7:30 am – Morning Prayers and Breakfast</li>
    <li>9:00 am – Keynote Address on Faith and Family</li>
    <li>10:30 am – Workshops for Teens and Parents</li>
    <li>12:00 pm – Lunch in the Parish Hall</li>
    <li>1:30 pm – Service Projects in the Community</li>
    <li>4:00 pm – Free Time and Sports</li>
    <li>6:00 pm – Vespers and Confession</li>
    <li>7:30 pm – Dinner and Talent Show</li>
    <li>9:30 pm – Evening Prayers</li>
  </ul>

  <div class="photo" role="img" aria-label="Icon of the patron saints" style="left:185px;top:110px;width:158px;height:70px;background:linear-gradient(160deg,#c9a45a,#8a5a2a)"></div>
  <div class="abs donate" style="left:185px;top:188px;width:158px;height:92px">
    <h3>DONATE</h3>
    <p>Your gift helps young people attend the gathering and grow in faith.</p>
    <span class="mark"><i></i>St. Luke's Youth Fund</span>
  </div>
  <div class="photo" role="img" aria-label="Photo of the parish church exterior" style="left:185px;top:290px;width:158px;height:140px;background:linear-gradient(180deg,#9fb6c8,#7c8a6a 55%,var(--photo-cool))"></div>

  <div class="abs strip">Questions? Contact the gathering office at the parish hall.</div>
</section>
<div class="page-label" style="left:228px;top:516px">PAGE 1</div>

<section class="page page-2">
  <ul class="abs agenda" style="left:12px;top:12px;width:170px">
    <h4>Saturday, October 10th</h4>
    <li>7:30 am – Divine Liturgy</li>
    <li>9:30 am – Breakfast and Announcements</li>
    <li>10:30 am – Panel Discussion for Youth</li>
    <li>12:30 pm – Lunch and Group Photo</li>
    <li>2:00 pm – Pilgrimage to Local Monastery</li>
    <li>6:00 pm – Great Vespers</li>
    <li>8:00 pm – Banquet and Awards Evening</li>
    <h4>Sunday, October 11th</h4>
    <li>9:00 am – Divine Liturgy and Procession</li>
    <li>12:00 pm – Farewell Luncheon</li>
    <li>1:30 pm – Departures and Safe Travels</li>
  </ul>

  <div class="photo" role="img" aria-label="Photo of participants gathered together" style="left:192px;top:12px;width:158px;height:78px;background:linear-gradient(135deg,#c7b79a,#7a6b55)"></div>
  <div class="abs body-text" style="left:192px;top:96px;width:158px">
    <p>Saturday evening brings our banquet with music, awards and shared stories.</p>
  </div>
  <div class="photo" role="img" aria-label="Photo of a theater stage with red curtains" style="left:192px;top:122px;width:158px;height:86px;background:linear-gradient(180deg,#3a0d0d,#9b1c1c 50%,#4a0f0f)"></div>

  <div class="abs band" style="left:192px;top:222px;width:158px;height:40px;font-size:12px">Other<br>Information</div>

  <div class="abs body-text" style="left:12px;top:280px;width:338px">
    <p><b>Lodging:</b> Lodging is available at nearby hotels with group rates for families.</p>
    <p><b>What to bring:</b> Please bring a Bible, modest attire and comfortable shoes.</p>
    <p><b>Meals:</b> Meals are provided for all registered guests during the gathering.</p>
    <p><b>Parking:</b> Free parking is available behind the fellowship hall and along the church lane.</p>
  </div>

  <div class="abs strip">Register early to reserve your place at the gathering.</div>
</section>
<div class="page-label" style="left:598px;top:516px">PAGE 2</div>

<section class="page page-3">
  <div class="photo" role="img" aria-label="Photo of green hills around the grounds" style="left:0;top:0;width:460px;height:110px;background:linear-gradient(180deg,#b9d39a,#6f9a45 60%,#3f6a25)"></div>
  <div class="abs band" style="left:28px;top:18px;width:130px;height:56px;font-size:13px">Description<br>of Event</div>

  <div class="abs body-text" style="left:22px;top:120px;width:416px">
    <p>The Faith and Fellowship Family Gathering brings families from many parishes together for three days of worship, learning and fellowship. Young people and parents share prayer, service and friendship while growing together in the life of the Church, guided by clergy and lay leaders from across the region.</p>
  </div>

  <div class="abs body-text faq" style="left:22px;top:168px;width:416px">
    <h4>FAQs</h4>
    <p><b>Who may attend?</b> The gathering is open to youth, parents, clergy and friends of every parish in our region. Guests from other communities are warmly welcome.</p>
    <p><b>How do I register?</b> Complete the registration form at the parish office and return it with your payment before the end of September so we can plan meals and lodging.</p>
    <p><b>Is there a cost?</b> A modest fee covers meals and materials, and scholarships are available for families who need support. Please ask the office in confidence.</p>
    <p><b>Where is it held?</b> All sessions take place at the parish church and the fellowship hall next door, with parking on site and shuttles to nearby hotels.</p>
    <p><b>Can I volunteer?</b> Yes, we welcome helpers for meals, music, setup and the Sunday procession. Please speak with the youth director after any service.</p>
    <p><b>What about children?</b> Supervised activities are offered for younger children during the workshops and the evening programs, led by trained volunteers.</p>
    <p><b>What should youth expect?</b> Talks, small group discussions, service projects, sports and plenty of time to make lasting friendships in faith.</p>
  </div>

  <div class="photo" role="img" aria-label="Photo of the church interior with icons" style="left:90px;top:400px;width:160px;height:80px;background:linear-gradient(135deg,#d9b56a,#8a5e28)"></div>
  <div class="abs body-text" style="left:90px;top:484px;width:160px">
    <p>Join us for a joyful weekend of faith.</p>
  </div>
  <div class="photo" role="img" aria-label="Photo of a priest greeting young people" style="left:320px;top:410px;width:118px;height:108px;background:linear-gradient(160deg,#cdbfa6,#6d6050)"></div>
</section>
<div class="page-label" style="left:418px;top:1140px">PAGE 3</div>

</body>
</html>
```